KLV [Naturally Renewable Goods]

We require a web design for a new line of products that we have created. The first of these is a product called B-GONE which is a natural product designed to repel animals such as Possums, snakes and Kangaroos in Australia and things like deer and Raccoons in the US.
Our Company and head office are in Sydney Australia and we have our own factories in Taiwan and China.
These items come in a few different forms such as Discs that can be thrown into a roof cavity, to a gell that comes in a PET container for use in the garden around plants and vegetables and an oil based spray that can be used on trucks of trees or plants and fences etc.
The final design should communicate an environmental and safe feeling for the user and also the animals it repels, but also make the user feel safe that they have B-goned the animals that were being a nuisance.

Target Market(s)

Home owners, gardeners, farmers

Industry/Entity Type

It Company

Requirements
Must have
• A green feeling that makes sure they understand that this product is a repellant and safe.
The Website must have the ability to grow outside the B-gone product line as new itmes are introduced such as Septic Bio products that break down waste and even make plants grow faster without chemicals.
Nice to have
• We already have a logo and trade mark for both KLV and B-gone which I will attach. The B-gone logo comes in different colours and animal images.
We were thinking of a name Meadow Wanderers as well but went with B-gone.
Should not have
• A green sell using the fonts etc included in the logos

```html
<!DOCTYPE html>
<html lang="en">
<head>
<meta charset="utf-8">
<title>KLV — Naturally Renewable Goods</title>
<link href="https://fonts.googleapis.com/css2?family=Arimo:wght@400;700&family=Noto+Sans:wght@400;700&display=swap" rel="stylesheet">
<style>
:root{
  --page-bg:#0b3d0b;
  --page-bg-dark:#052405;
  --leaf:#8dc63f;
  --leaf-light:#a8d85a;
  --leaf-deep:#5c9a5c;
  --bar-top:#3d3d3d;
  --bar-bottom:#1c1c1c;
  --white:#ffffff;
  --ink:#222222;
  --body:#444444;
  --muted:#cccccc;
  --alert:#c00000;
  --footer:#333333;
}
*{margin:0;padding:0;box-sizing:border-box}
html,body{width:1023px;height:1200px;overflow:hidden}
body{background:radial-gradient(ellipse at center,var(--page-bg) 0%,var(--page-bg-dark) 100%);font-family:"Noto Sans",sans-serif;position:relative;color:var(--body)}
.site{position:absolute;left:37px;top:10px;width:936px;height:1162px;background:var(--white);border-radius:4px;overflow:hidden}
.abs{position:absolute}
.masthead{left:0;top:0;width:936px;height:103px;background:var(--leaf)}
.brand{left:44px;top:16px;color:var(--white);font-family:"Noto Sans",sans-serif;font-weight:700}
.brand-name{font-size:50px;line-height:56px}
.brand-tag{font-size:11px;margin-top:4px;margin-left:2px}
.login{left:826px;top:28px;display:flex;align-items:center;gap:10px;color:var(--white);font-family:"Arimo",sans-serif;font-size:12px}
.login-avatar{width:19px;height:28px;border-radius:3px;background:linear-gradient(#e8a070,#2a6fb0)}
.navbar{left:0;top:103px;width:936px;height:37px;background:linear-gradient(var(--bar-top),var(--bar-bottom))}
.search{left:20px;top:7px;width:211px;height:21px;background:var(--white);border-radius:11px;box-shadow:inset 0 1px 3px #888}
.search svg{position:absolute;left:5px;top:3px}
.go{left:247px;top:8px;width:34px;height:20px;border-radius:3px;background:linear-gradient(var(--leaf-light),#4f8f2f);color:var(--white);font-family:"Arimo",sans-serif;font-size:11px;text-align:center;line-height:20px}
.nav-divider{left:419px;top:0;width:1px;height:37px;background:#555}
.menu{left:0;top:0;width:936px;height:37px;font-family:"Arimo",sans-serif;font-size:11.5px;color:var(--white)}
.menu span{position:absolute;top:12px}
.menu .sep{color:#aaa}
.menu .active{color:var(--leaf)}
.hero{left:6px;top:147px;width:924px;height:375px;background:linear-gradient(90deg,#8a6a3a 0%,#c7a36a 35%,#e6cfa4 60%,#8c7a60 80%,#d9c29a 100%)}
.arrow{top:312px;width:29px;height:29px;background:#000;border:1px solid #ccc}
.arrow svg{position:absolute;left:7px;top:6px}
.hero-badge{left:55px;top:388px;width:161px;height:88px;background:var(--white);border-radius:5px;display:flex;align-items:center;justify-content:center;gap:8px;font-family:"Arimo",sans-serif;font-weight:700;font-size:26px;color:var(--ink)}
.ring{border-radius:50%;background:var(--ink)}
.hero-copy{left:249px;top:390px;width:462px;font-family:"Arimo",sans-serif;font-size:16px;line-height:22.5px;color:var(--white)}
.tab{height:37px;background:linear-gradient(var(--leaf-light),var(--leaf-deep));border-radius:3px 3px 0 0}
.welcome-tab{left:16px;top:525px;width:206px;padding-left:12px;font-size:24px;line-height:37px;color:var(--ink)}
.welcome-tab em{font-style:normal;color:var(--leaf-light)}
.panel{border:6px solid;border-image:linear-gradient(var(--leaf-light),var(--leaf-deep)) 1;background:var(--white)}
.welcome-panel{left:14px;top:563px;width:558px;height:234px;padding:26px 14px 0 20px;font-size:12px;letter-spacing:0.15px;line-height:22.3px;color:var(--body)}
.welcome-panel p+p{margin-top:19px}
.product-tab{left:592px;top:525px;width:206px;text-align:center;font-size:16px;line-height:42px;color:var(--ink)}
.product-panel{left:591px;top:563px;width:335px;height:234px}
.product-mark{position:absolute;left:30px;top:60px;display:flex;align-items:center;gap:14px;font-family:"Arimo",sans-serif;font-weight:700;font-size:44px;color:var(--ink)}
.view{position:absolute;right:12px;bottom:8px;font-size:15px;color:var(--alert)}
.col-title{top:826px;font-size:16px;font-weight:400;color:var(--ink)}
.who-sub{left:61px;top:872px;font-size:15px;font-weight:400;color:var(--ink)}
.who-copy{left:61px;top:905px;width:205px;font-size:12.5px;line-height:19.5px;color:var(--body)}
.btn{border-radius:3px;background:linear-gradient(var(--leaf-light),#4f8f2f);text-align:center;font-size:13px;color:var(--ink)}
.view-more{left:81px;top:1025px;width:102px;height:29px;line-height:29px}
.quote-avatar{left:363px;width:34px;height:34px;background:linear-gradient(#e4e4e4,#cfcfcf);border-radius:2px}
.quote{left:415px;width:150px;font-family:"Arimo",sans-serif;font-size:10.5px;line-height:16.7px;color:var(--ink)}
.quote .more{display:block;margin:8px 0 0 7px;color:var(--alert);font-size:10px}
.field{left:673px;width:186px;height:31px;border:1px solid #999;background:linear-gradient(#fafafa,#c9c9c9);padding-left:16px;line-height:29px;font-size:12px;color:var(--ink)}
.subscribe{left:694px;top:981px;width:102px;height:29px;line-height:29px}
.footer{left:0;top:1089px;width:936px;height:73px;background:var(--footer)}
.social{top:24px;width:15px;height:15px;border-radius:2px}
.footer-links{left:0;top:16px;width:976px;text-align:center;font-family:"Arimo",sans-serif;font-size:11px;color:var(--muted)}
.footer-links .sep{margin:0 14px}
.copyright{left:0;top:39px;width:976px;text-align:center;font-family:"Arimo",sans-serif;font-size:11px;color:var(--muted)}
</style>
</head>
<body>
<div class="site">
  <header class="abs masthead">
    <div class="abs brand">
      <div class="brand-name">KLV</div>
      <div class="brand-tag">Naturally Renewable Goods</div>
    </div>
    <div class="abs login"><span class="login-avatar" role="img" aria-label="User account icon"></span>LOGIN</div>
  </header>

  <nav class="abs navbar">
    <div class="abs search">
      <svg width="16" height="16" viewBox="0 0 16 16"><circle cx="6.5" cy="6.5" r="4.5" fill="none" stroke="#c86a2a" stroke-width="2"/><line x1="10" y1="10" x2="14" y2="14" stroke="#555" stroke-width="2.5"/></svg>
    </div>
    <div class="abs go">Go</div>
    <div class="abs nav-divider"></div>
    <div class="abs menu">
      <span class="active" style="left:460px">HOME</span><span class="sep" style="left:512px">|</span>
      <span style="left:533px">ABOUT US</span><span class="sep" style="left:609px">|</span>
      <span style="left:627px">SERVICES</span><span class="sep" style="left:702px">|</span>
      <span style="left:730px">GALLERY</span><span class="sep" style="left:800px">|</span>
      <span style="left:818px">CONTACT US</span>
    </div>
  </nav>

  <section class="abs hero" role="img" aria-label="Photo of cats beside a pet cage and a rodent peeking from a hole"></section>
  <div class="abs arrow" style="left:6px"><svg width="14" height="16" viewBox="0 0 14 16"><polyline points="10,1 3,8 10,15" fill="none" stroke="#fff" stroke-width="3"/></svg></div>
  <div class="abs arrow" style="left:902px"><svg width="14" height="16" viewBox="0 0 14 16"><polyline points="4,1 11,8 4,15" fill="none" stroke="#fff" stroke-width="3"/></svg></div>
  <div class="abs hero-badge"><span class="ring" style="width:24px;height:24px"></span>B-gone</div>
  <p class="abs hero-copy">Lorem ipsum dolor sit amet, consectetuer adipiscing elit. Nam nibh. Nunc varius facilisis eros. Sed erat.In in velit quis arcuornare laoreet. Curabitur adipiscing luctus massa.Integer purus ac augue commodo commodo.</p>

  <div class="abs tab welcome-tab">Welcome to <em>KLV</em></div>
  <div class="abs panel welcome-panel">
    <p>Lorem ipsum dolor sit amet, adipiscing elit. Nam nibh. Nunc varius facilisis eros. Sed erat.In in velit quis arcuornare laoreet. Curabitur adipiscing luctus massa.Integer ut purus ac commodo commodo. Lorem ipsum dolor sit amet, adipiscing elit. Nam nibh. Nunc varius facilisis eros. Sed erat.In in velit quis arcuornare laoreet. Curabitur adipiscing luctus massa.Integer ut purus ac commodo commodo.</p>
    <p>Lorem ipsum dolor sit amet, adipiscing elit. Nam nibh. Nunc varius facilisis eros. Sed erat.In in velit quis arcuornare laoreet. Curabitur adipiscing luctus massa.</p>
  </div>

  <div class="abs tab product-tab">OUR PRODUCT</div>
  <div class="abs panel product-panel">
    <div class="product-mark"><span class="ring" style="width:80px;height:80px"></span>B-gone</div>
    <span class="view">&gt;&gt; VIEW</span>
  </div>

  <h3 class="abs col-title" style="left:87px">WHO WE ARE</h3>
  <h4 class="abs who-sub">Lorem ipsum dolor sit amet</h4>
  <p class="abs who-copy">Lorem ipsum dolor sit amet, adipiscing elit. Nam nibh. Nunc varius facilisis eros. Sed erat.In in velit quis arcuornare laoreet. Curabitur adipiscing luctus massa.</p>
  <div class="abs btn view-more">View More</div>

  <h3 class="abs col-title" style="left:372px">TESTIMONIALS</h3>
  <div class="abs quote-avatar" style="top:872px" role="img" aria-label="Customer portrait placeholder"></div>
  <p class="abs quote" style="top:864px">Lorem Ipsum is simply dummy text Lorem Ipsum is simply Lorem Ipsum is simply dummy text Lorem Ipsum is simply<span class="more">More</span></p>
  <div class="abs quote-avatar" style="top:985px" role="img" aria-label="Customer portrait placeholder"></div>
  <p class="abs quote" style="top:977px">Lorem Ipsum is simply dummy text Lorem Ipsum is simply Lorem Ipsum is simply dummy text Lorem Ipsum is simply<span class="more">More</span></p>

  <h3 class="abs col-title" style="left:675px">NEWSLETTER</h3>
  <div class="abs field" style="top:873px">User Name</div>
  <div class="abs field" style="top:921px">Your Email Id</div>
  <div class="abs btn subscribe">Subscribe</div>

  <footer class="abs footer">
    <span class="abs social" style="left:30px;background:#3b5998"></span>
    <span class="abs social" style="left:58px;background:#33aadd"></span>
    <span class="abs social" style="left:85px;background:#f26a1b"></span>
    <div class="abs footer-links">Privacy Policy<span class="sep">|</span>Terms and Conditions<span class="sep">|</span>Contact Us</div>
    <div class="abs copyright">Copyright 2011 KLV,&nbsp; All Rights Reserved</div>
  </footer>
</div>
</body>
</html>
```